Tall Harbor Business Card

We are a Video Production and Video Equipment Rental company specialising in the supply of state of the art Video Technology and Services for the Live Entertainment, Television and Corporate Business Theatre markets. (in Sydney, Australia) www.tallharbor-media.example

Industry/Entity Type

Business

Contact Information for Business Card

name, position, email, website, address, logo
Example attached of the information we need - doesn't necessarily have to look the same

Font styles to use
Other font styles liked:
• Tall Harbor logo font is GOTHAM

Colors
ea1f27

Requirements
Nice to have
• either matt black or shiny black cards -
raised logo

```html
<!DOCTYPE html>
<html lang="en">
<head>
<meta charset="utf-8">
<title>Tall Harbor Business Card</title>
<link rel="stylesheet" href="https://fonts.googleapis.com/css2?family=Arimo:wght@400;700&display=swap">
<style>
  :root {
    --page-bg: #e4e4e4;
    --card-bg: #1a1a1a;
    --band-bg: #000000;
    --brand-red: #ea1f27;
    --text-white: #ffffff;
    --rule-grey: #6e6e6e;
  }
  * { margin: 0; padding: 0; box-sizing: border-box; }
  html, body {
    width: 1012px;
    height: 1200px;
    overflow: hidden;
    background: var(--page-bg);
    font-family: "Arimo", Arial, sans-serif;
  }
  .canvas { position: relative; width: 1012px; height: 1200px; }

  .card {
    position: absolute;
    left: 110px;
    width: 808px;
    height: 472px;
    background: var(--card-bg);
    overflow: hidden;
  }
  .card--front { top: 102px; }
  .card--back  { top: 632px; }

  /* Front */
  .front-band {
    position: absolute;
    left: 0; top: 138px;
    width: 100%; height: 187px;
    background: var(--band-bg);
  }
  .front-wordmark {
    position: absolute;
    left: 0; top: 138px;
    width: 100%; height: 187px;
    display: flex; align-items: center; justify-content: center;
    color: var(--text-white);
    font-weight: 400;
    font-size: 74px;
    letter-spacing: 2px;
    text-transform: uppercase;
  }
  .services {
    position: absolute;
    left: 0; top: 370px;
    width: 100%;
    text-align: center;
    font-size: 15.5px;
    color: var(--brand-red);
    text-transform: uppercase;
    letter-spacing: 0.2px;
  }
  .services .sep { color: var(--text-white); margin: 0 10px; }

  /* Back */
  .back-wordmark {
    position: absolute;
    left: 51px; top: 86px;
    color: var(--text-white);
    font-size: 34px;
    font-weight: 400;
    letter-spacing: 1px;
    text-transform: uppercase;
  }
  .name-rule {
    position: absolute;
    left: 51px; top: 262px;
    width: 498px; height: 2px;
    background: var(--rule-grey);
  }
  .holder-name {
    position: absolute;
    right: 76px; top: 248px;
    color: var(--text-white);
    font-size: 24px;
  }
  .holder-role {
    position: absolute;
    right: 76px; top: 287px;
    color: var(--brand-red);
    font-size: 14.5px;
  }
  .contact-online {
    position: absolute;
    right: 270px; top: 330px;
    text-align: right;
    color: var(--text-white);
    font-size: 15px;
    line-height: 24px;
  }
  .contact-divider {
    position: absolute;
    left: 560px; top: 330px;
    width: 2px; height: 50px;
    background: var(--brand-red);
  }
  .contact-address {
    position: absolute;
    right: 76px; top: 330px;
    text-align: right;
    color: var(--text-white);
    font-size: 15px;
    line-height: 24px;
  }
  .foot-band {
    position: absolute;
    left: 0; bottom: 0;
    width: 100%; height: 20px;
    background: var(--brand-red);
  }
</style>
</head>
<body>
<main class="canvas">
  <section class="card card--front" aria-label="Card front">
    <div class="front-band"></div>
    <div class="front-wordmark">Tall Harbor</div>
    <p class="services">
      Video Solution<span class="sep">-</span>LED Screens<span class="sep">-</span>Camera Systems<span class="sep">-</span>Projection
    </p>
  </section>

  <section class="card card--back" aria-label="Card back">
    <div class="back-wordmark">Tall Harbor</div>
    <div class="name-rule"></div>
    <h1 class="holder-name">Mark Delaney</h1>
    <p class="holder-role">Managing Director</p>
    <address class="contact-online" style="font-style:normal">
      mark@tallharbor-media.example<br>
      www.tallharbor-media.example
    </address>
    <div class="contact-divider"></div>
    <address class="contact-address" style="font-style:normal">
      18 Quay Lane, Mascot<br>
      NSW 2020, Australia
    </address>
    <div class="foot-band"></div>
  </section>
</main>
</body>
</html>
```